Flyer für Anbieter von Haushaltshilfen und Alltagsbegleitern für Privathaushalte
Zielgruppe
Wir bieten Haushaltshilfen und Alltagsbegleiter für Privathaushalte an. Unsere Hauptkundenklientel sind Pflegebedürftige Menschen denen eine Haushaltshilfe von der Pflegekasse zusteht. Weitere Kunden sind Familien und/oder Singlehaushalte, die eine Haushaltfshilfe benötigen.
Aufgabenstellung
- Erstellung neues Design eines Flyers 105x210
- Es sollen hauptsächlich unsere Logofarben Rot und Grau verwendet werden

```html
<!DOCTYPE html>
<html lang="de">
<head>
<meta charset="utf-8">
<title>Lindmark – Flyer Haushaltshilfen</title>
<link rel="stylesheet" href="https://fonts.googleapis.com/css2?family=Cinzel:wght@500;700;800&family=Poppins:wght@400;500;600;700;800&display=swap">
<style>
:root{
  --red:#c01f2f;
  --red-dark:#a51826;
  --ink:#1d1b1c;
  --gray-text:#4a4a4a;
  --gray-band:#d7d7d9;
  --white:#ffffff;
  --stage:#e4e4e6;
}
*{margin:0;padding:0;box-sizing:border-box}
html,body{width:1101px;height:1200px;overflow:hidden}
body{background:var(--stage);position:relative;font-family:"Poppins",sans-serif}
.flyer{position:absolute;top:80px;width:520px;height:1040px;background:var(--red);overflow:hidden;box-shadow:0 6px 18px rgba(0,0,0,.18)}
.flyer--front{left:20px}
.flyer--back{left:561px}
.flyer__bg{position:absolute;inset:0;width:520px;height:1040px}
.abs{position:absolute}

/* brand */
.brand{display:flex;align-items:center;gap:14px}
.brand__dot{border:5px solid var(--red);border-radius:50%;flex:none}
.brand__name{font-family:"Cinzel",serif;font-weight:700;color:#3a3a3a;letter-spacing:1px;white-space:nowrap}
.brand--top{left:84px;top:32px}
.brand--top .brand__dot{width:80px;height:80px}
.brand--top .brand__name{font-size:44px}
.brand--small{left:360px;top:912px;width:120px;flex-direction:column;gap:8px}
.brand--small .brand__dot{width:50px;height:50px;border-width:4px}
.brand--small .brand__name{font-size:17px}

/* front */
.alert{left:0;width:520px;top:140px;text-align:center;font-weight:800;color:var(--red);font-size:29px;line-height:32px;letter-spacing:-.5px}
.hero-title{left:0;width:520px;top:562px;text-align:center;color:var(--white);font-family:"Cinzel",serif}
.hero-title__lead{display:block;font-weight:700;font-size:30px;line-height:31px}
.hero-title__main{display:block;font-weight:800;font-size:49px;line-height:51px;margin-top:10px}
.underline{left:120px;top:798px}
.front-note{left:40px;width:440px;top:880px;text-align:center;font-size:16.5px;line-height:21px;color:var(--ink)}
.front-note strong{color:var(--red);font-weight:700}
.url-band{left:0;bottom:0;width:520px;height:60px;background:var(--gray-band);display:flex;align-items:center;justify-content:center;font-family:"Cinzel",serif;font-weight:500;font-size:20px;color:var(--red);letter-spacing:1px}

/* back */
.tab{left:0;top:41px;width:378px;height:45px;background:var(--ink);border-radius:0 24px 24px 0;color:var(--white);font-family:"Cinzel",serif;font-weight:800;font-size:27px;display:flex;align-items:center;padding-left:86px}
.benefit{width:190px;text-align:center}
.benefit__icon{width:80px;height:80px;border-radius:50%;background:var(--red);margin:0 auto;display:flex;align-items:center;justify-content:center}
.benefit__text{margin-top:6px;font-weight:600;font-size:13.5px;line-height:16px;color:var(--gray-text)}
.benefit--a{left:104px;top:101px}
.benefit--b{left:300px;top:101px}
.benefit--c{left:104px;top:234px}
.benefit--d{left:300px;top:234px}
.about{left:62px;width:396px;top:566px;text-align:center;color:var(--white);font-size:13px;line-height:16.8px}
.about p+p{margin-top:16px}
.about-title{left:40px;width:440px;top:750px;text-align:center;color:var(--white);font-family:"Cinzel",serif;font-weight:800;font-size:21px;line-height:23px}
.cta{left:45px;top:886px;color:var(--red);font-weight:700;font-size:18px}
.contact{display:flex;align-items:center;gap:9px;font-size:14.5px;font-weight:600;color:var(--ink);white-space:nowrap}
.contact--plain{font-weight:400}
.contact svg{flex:none}
.c1{left:46px;top:922px}.c2{left:210px;top:922px}
.c3{left:46px;top:951px}.c4{left:210px;top:951px}
.c5{left:46px;top:981px}
</style>
</head>
<body>

<section class="flyer flyer--front">
  <svg class="flyer__bg" viewBox="0 0 520 1040" aria-hidden="true">
    <defs>
      <clipPath id="frontOval"><path d="M46,0 C20,300 100,535 310,548 C400,552 470,520 520,485 L520,0 Z"/></clipPath>
      <linearGradient id="frontPhoto" x1="0" y1="0" x2="0.25" y2="1">
        <stop offset="0" stop-color="#ffffff"/>
        <stop offset=".25" stop-color="#f3e6dc"/>
        <stop offset=".5" stop-color="#d39a7a"/>
        <stop offset=".78" stop-color="#6a5650"/>
        <stop offset="1" stop-color="#2a2626"/>
      </linearGradient>
    </defs>
    <path d="M46,0 C20,300 100,535 310,548 C400,552 470,520 520,485 L520,0 Z" fill="#fff" stroke="#1d1b1c" stroke-width="10"/>
    <rect x="0" y="220" width="520" height="340" fill="url(#frontPhoto)" clip-path="url(#frontOval)" role="img" aria-label="Foto: junge Hand hält die Hand einer älteren Person"/>
    <path d="M0,790 C130,855 340,860 520,778 L520,1040 L0,1040 Z" fill="#fff"/>
    <path d="M0,790 C130,855 340,860 520,778" fill="none" stroke="#1d1b1c" stroke-width="7"/>
  </svg>

  <div class="abs brand brand--top"><span class="brand__dot"></span><span class="brand__name">LINDMARK</span></div>

  <p class="abs alert">VERSCHENKEN SIE<br>NICHT IHR GELD!!</p>

  <h1 class="abs hero-title">
    <span class="hero-title__lead">HAUSHALTSHILFEN UND<br>ALLTAGSBEGLEITER</span>
    <span class="hero-title__main">BENÖTIGEN<br>SIE HILFE<br>IM HAUSHALT?</span>
  </h1>
  <svg class="abs underline" width="260" height="22" viewBox="0 0 260 22" aria-hidden="true">
    <path d="M3,16 C80,10 180,6 252,4 C220,9 190,12 160,15 C175,14 190,15 175,18" fill="none" stroke="#fff" stroke-width="4" stroke-linecap="round"/>
  </svg>

  <p class="abs front-note">Nutzen Sie Ihren <strong>Entlastungsbetrag</strong><br><strong>ab Pflegegrad 1</strong> und Ihre <strong>Verhinderungspflege</strong><br><strong>ab dem Pflegegrad 2,</strong> bevor Ihr<br>Anspruch verfällt</p>

  <div class="abs url-band">WWW.LINDMARK.DE</div>
</section>

<section class="flyer flyer--back">
  <svg class="flyer__bg" viewBox="0 0 520 1040" aria-hidden="true">
    <defs>
      <clipPath id="backOval"><path d="M52,0 C35,300 110,535 320,548 C410,552 475,515 520,480 L520,0 Z"/></clipPath>
      <linearGradient id="backPhoto" x1="0" y1="0" x2="0.6" y2="1">
        <stop offset="0" stop-color="#ffffff"/>
        <stop offset=".3" stop-color="#ececee"/>
        <stop offset=".6" stop-color="#b5b5b9"/>
        <stop offset=".85" stop-color="#4a4a4c"/>
        <stop offset="1" stop-color="#e8773a"/>
      </linearGradient>
    </defs>
    <path d="M52,0 C35,300 110,535 320,548 C410,552 475,515 520,480 L520,0 Z" fill="#fff" stroke="#1d1b1c" stroke-width="10"/>
    <rect x="0" y="385" width="520" height="175" fill="url(#backPhoto)" clip-path="url(#backOval)" role="img" aria-label="Foto: Polster wird mit einem Waschsauger gereinigt"/>
    <path d="M0,790 C130,855 340,860 520,778 L520,1040 L0,1040 Z" fill="#fff"/>
    <path d="M0,790 C130,855 340,860 520,778" fill="none" stroke="#1d1b1c" stroke-width="7"/>
  </svg>

  <h2 class="abs tab">UNSERE VORTEILE</h2>

  <div class="abs benefit benefit--a">
    <div class="benefit__icon">
      <svg width="40" height="46" viewBox="0 0 40 46" fill="none" stroke="#fff" stroke-width="3" stroke-linejoin="round"><path d="M6,3 H34 V42 L29,38 L24,42 L20,38 L16,42 L11,38 L6,42 Z"/><text x="20" y="27" fill="#fff" stroke="none" font-family="Poppins,sans-serif" font-weight="700" font-size="18" text-anchor="middle">$</text><path d="M13,33 H27"/></svg>
    </div>
    <p class="benefit__text">Abrechnung mit allen<br>Pflegekassen möglich</p>
  </div>
  <div class="abs benefit benefit--b">
    <div class="benefit__icon">
      <svg width="46" height="44" viewBox="0 0 46 44" fill="none" stroke="#fff" stroke-width="3" stroke-linejoin="round" stroke-linecap="round"><path d="M23,20 C14,13 12,8 15,5 C18,2 22,4 23,7 C24,4 28,2 31,5 C34,8 32,13 23,20 Z"/><path d="M3,32 L12,26 C16,24 19,25 22,27 H30 C33,27 33,31 30,31 H21 M30,31 L40,25 C43,24 45,27 42,30 L30,39 H12 L6,42"/></svg>
    </div>
    <p class="benefit__text">Auch über die<br>Verhinderungspflege</p>
  </div>
  <div class="abs benefit benefit--c">
    <div class="benefit__icon">
      <svg width="46" height="42" viewBox="0 0 46 42" fill="none" stroke="#fff" stroke-width="3.5" stroke-linejoin="round" stroke-linecap="round"><path d="M22,36 C8,25 3,18 4,11 C5,4 14,1 21,8 C28,1 38,4 39,12"/><path d="M35,22 V38 M27,30 H43"/></svg>
    </div>
    <p class="benefit__text">Abrechnung über<br>den Entlastungsbetrag<br>von mind. 125 € mtl.<br>ab Pflegegrad 1 möglich</p>
  </div>
  <div class="abs benefit benefit--d">
    <div class="benefit__icon">
      <svg width="40" height="44" viewBox="0 0 40 44" fill="none" stroke="#fff" stroke-width="3" stroke-linejoin="round" stroke-linecap="round"><path d="M26,40 H8 C5,40 4,38 4,36 V7 C4,5 5,4 8,4 H26 C29,4 30,5 30,7 V16"/><path d="M10,12 H24 M10,19 H24 M10,26 H18"/><path d="M22,36 L34,22 L38,26 L26,40 L21,41 Z"/></svg>
    </div>
    <p class="benefit__text">Hilfe bei der<br>Antragsstellung</p>
  </div>

  <div class="abs about">
    <p>Um Älteren oder beeinträchtigten Menschen ein Leben in ihrem sozialen Umfeld zu ermöglichen, bedarf es der Unterstützung im Alltag. Die dabei täglich anfallenden Aufgaben des Haushalts können oft belastend sein und die Pflege der betroffenen Personen erschweren.</p>
    <p>Um sie zu entlasten, bieten wir Ihnen bedarfsorientierte Hilfe rund um den Haushalt an. Mit unserem breiten Spektrum an Services möchten wir Sie beim bewältigen des Alltags unterstützen.</p>
  </div>

  <h3 class="abs about-title">SIE SIND PFLEGEBEDÜRFTIG<br>UND BENÖTIGEN HILFE<br>IM HAUSHALT?</h3>

  <p class="abs cta">Jetzt kostenlos beraten lassen!</p>

  <div class="abs contact c1"><svg width="13" height="13" viewBox="0 0 16 16"><circle cx="8" cy="8" r="8" fill="#c01f2f"/><path d="M5,4 L7,6 L6,7.5 C7,9 8,10 9.5,11 L11,10 L12.5,12 C11,13.5 9,13 7,11 C5,9 3.5,6 5,4 Z" fill="#fff"/></svg>0711 20 38 47 19</div>
  <div class="abs contact c2"><svg width="13" height="13" viewBox="0 0 16 16"><circle cx="8" cy="8" r="8" fill="#c01f2f"/><path d="M5,4 L7,6 L6,7.5 C7,9 8,10 9.5,11 L11,10 L12.5,12 C11,13.5 9,13 7,11 C5,9 3.5,6 5,4 Z" fill="#fff"/></svg>0176 58 13 94 27</div>
  <div class="abs contact c3"><svg width="13" height="13" viewBox="0 0 16 16"><circle cx="8" cy="8" r="8" fill="#c01f2f"/><rect x="4" y="5" width="8" height="6" fill="none" stroke="#fff" stroke-width="1.2"/><path d="M4,5 L8,8.5 L12,5" fill="none" stroke="#fff" stroke-width="1.2"/></svg>info@lindmark.de</div>
  <div class="abs contact c4"><svg width="13" height="13" viewBox="0 0 16 16"><circle cx="8" cy="8" r="8" fill="#c01f2f"/><circle cx="8" cy="8" r="4.5" fill="none" stroke="#fff" stroke-width="1.1"/><ellipse cx="8" cy="8" rx="2" ry="4.5" fill="none" stroke="#fff" stroke-width="1.1"/><path d="M3.5,8 H12.5" stroke="#fff" stroke-width="1.1"/></svg>www.lindmark.de</div>
  <div class="abs contact contact--plain c5"><svg width="12" height="15" viewBox="0 0 12 16"><path d="M6,0 C2.7,0 0,2.6 0,6 C0,10 6,16 6,16 C6,16 12,10 12,6 C12,2.6 9.3,0 6,0 Z" fill="#c01f2f"/><circle cx="6" cy="6" r="2.3" fill="#fff"/></svg>Lindenweg 14, 73730 Esslingen</div>

  <div class="abs brand brand--small"><span class="brand__dot"></span><span class="brand__name">LINDMARK</span></div>
</section>

</body>
</html>
```